" Montamos roteiros turisticos especializados em experiência. Inicialmente a empresa ofertará roteiros especializados para fotografia, porém no futuro poderá conter roteiros para vinhos, culinária, esportes, etc. "

```html
<!DOCTYPE html>
<html lang="pt-BR">
<head>
<meta charset="UTF-8">
<title>Lumira Expedições — Tire suas dúvidas</title>
<link href="https://fonts.googleapis.com/css2?family=Open+Sans:wght@400;600;700;800&display=swap" rel="stylesheet">
<style>
  :root {
    --blue: #2a8fd2;
    --blue-dark: #1c6fa8;
    --orange: #f2a12e;
    --ink: #3a3f45;
    --muted: #7a8088;
    --line: #e3e6ea;
    --white: #ffffff;
    --page: #f6f7f9;
    --hero-a: #1b2a44;
    --hero-b: #5a6f8c;
    --hero-c: #c98a4a;
  }
  * { box-sizing: border-box; margin: 0; padding: 0; }
  html, body { width: 1200px; height: 1200px; overflow: hidden; }
  body { font-family: "Open Sans", Arial, sans-serif; background: var(--white); color: var(--ink); }

  .topbar { height: 44px; background: var(--blue); display: flex; align-items: center; justify-content: space-between; padding: 0 60px; color: var(--white); font-size: 14px; }
  .social { display: flex; gap: 14px; }
  .social span { width: 14px; height: 14px; border-radius: 50%; background: rgba(255,255,255,.85); display: block; }
  .contact { display: flex; gap: 26px; align-items: center; }
  .contact .item { display: flex; gap: 6px; align-items: center; }

  .header { height: 110px; display: flex; align-items: center; justify-content: space-between; padding: 0 60px; border-bottom: 1px solid var(--line); }
  .brand { display: flex; align-items: center; gap: 12px; font-size: 34px; font-weight: 700; color: var(--blue-dark); }
  .brand .dot { width: 40px; height: 40px; border-radius: 50%; background: var(--orange); }
  .nav { display: flex; gap: 34px; align-items: center; font-size: 14px; font-weight: 700; color: var(--ink); letter-spacing: .3px; }
  .nav .home { width: 20px; height: 20px; }

  .hero { position: relative; height: 440px; background: linear-gradient(180deg, var(--hero-a) 0%, var(--hero-b) 45%, var(--hero-c) 100%); }
  .hero-text { position: absolute; left: 60px; top: 170px; color: var(--white); }
  .hero-text h1 { font-size: 52px; font-weight: 800; letter-spacing: 1px; }
  .hero-text p { font-size: 16px; margin-top: 8px; opacity: .9; }

  .content { display: flex; gap: 50px; padding: 50px 60px; }
  .sidebar { width: 320px; }
  .sidebar h2 { font-size: 24px; font-weight: 600; color: var(--blue); padding-bottom: 16px; border-bottom: 2px solid var(--line); }
  .cat { display: flex; justify-content: space-between; align-items: center; padding: 20px 0; border-bottom: 1px solid var(--line); font-size: 15px; color: var(--muted); }
  .cat .arrow { color: var(--orange); font-weight: 700; }

  .topics { flex: 1; }
  .topics h2 { font-size: 24px; font-weight: 600; color: var(--orange); padding-bottom: 16px; border-bottom: 2px solid var(--line); }
  .question { display: flex; align-items: center; gap: 12px; margin-top: 22px; font-size: 19px; font-weight: 700; color: var(--blue-dark); }
  .question svg { flex: none; }
  .answer { margin-top: 18px; font-size: 16px; line-height: 1.8; color: var(--muted); }
</style>
</head>
<body>
  <div class="topbar">
    <div class="social"><span></span><span></span><span></span><span></span><span></span></div>
    <div class="contact">
      <div class="item">
        <svg width="14" height="14" viewBox="0 0 24 24" fill="none" stroke="#fff" stroke-width="2"><path d="M5 3h4l2 5-2.5 1.5a11 11 0 0 0 6 6L16 13l5 2v4a2 2 0 0 1-2 2A16 16 0 0 1 3 5a2 2 0 0 1 2-2z"/></svg>
        (00) 0000-0000
      </div>
      <div class="item">
        <svg width="16" height="14" viewBox="0 0 24 20" fill="none" stroke="#fff" stroke-width="2"><rect x="2" y="2" width="20" height="16" rx="2"/><path d="M2 4l10 7 10-7"/></svg>
        email@email.com
      </div>
      <div class="item">Entrar</div>
      <div class="item">Cadastre-se</div>
    </div>
  </div>

  <header class="header">
    <div class="brand"><span class="dot"></span>Lumira Expedições</div>
    <nav class="nav">
      <svg class="home" viewBox="0 0 24 24" fill="none" stroke="#2a8fd2" stroke-width="2"><path d="M3 11l9-8 9 8"/><path d="M5 10v10h14V10"/></svg>
      <span>SOBRE NÓS</span>
      <span>PRÓXIMAS EXPEDIÇÕES</span>
      <span>ÚLTIMAS VIAGENS</span>
      <span>FAQ</span>
      <span>CONTATO</span>
      <svg width="20" height="20" viewBox="0 0 24 24" fill="none" stroke="#2a8fd2" stroke-width="2.5"><circle cx="10" cy="10" r="7"/><path d="M15 15l6 6"/></svg>
    </nav>
  </header>

  <section class="hero" role="img" aria-label="Foto noturna de uma vila alpina coberta de neve com luzes acesas">
    <div class="hero-text">
      <h1>TIRE SUAS DÚVIDAS</h1>
      <p>Início » FAQ</p>
    </div>
  </section>

  <main class="content">
    <aside class="sidebar">
      <h2>Categorias</h2>
      <div class="cat">EXPEDIÇÕES <span class="arrow">›</span></div>
      <div class="cat">VIAGENS <span class="arrow">›</span></div>
    </aside>
    <section class="topics">
      <h2>Tópicos</h2>
      <div class="question">
        <svg width="24" height="24" viewBox="0 0 24 24"><circle cx="12" cy="12" r="11" fill="#f2a12e"/><path d="M10 7l5 5-5 5" fill="none" stroke="#fff" stroke-width="2.5"/></svg>
        Sou iniciante na fotografia. Posso participar de uma expedição?
      </div>
      <p class="answer">Com certeza! Todos são bem-vindos, nossos grupos levam iniciantes ou profissionais. Buscaremos entender o perfil de cada participante para que o fotógrafo responsável pela viagem transmita as orientações adequadas a cada nível, do ajuste básico da câmera às técnicas de composição em campo.</p>
    </section>
  </main>
</body>
</html>
```